Vermilion Reel Works Web Design

COMPANY: VERMILION REEL WORKS
LOCATION: SHANGHAI, CHINA
AREA: FILM/TV DRAMA/COMMERCIALS/GAME POST PRODUCTION, SOUND DESIGN, MUSIC, and GAME.
WEB STYLE: SIMPLE, PROFESSIONAL, TRUSTWORTHY

LANGUAGE: ENGLISH, CHINESE. (Same layout, different language)
UPDATE: AFTER PROJECT FINISHED, WE NEED UPDATE BY OURSELVES.

MAIN SUBJECT: 6
1 HOMEPAGE
2 ABOUT US
3 TEAM
4 SERVICES
5 FACILITY
6 CONTACT

add one page of JOB OPPORTUNITIES.

DETAILS
1 HOMEPAGE
SLOGAN: Vermilion Reel Works provides a well-designed working environment which amplifies your team’s ability to reach their creative goals.

Our services include:
 Feature Films
 Music & Scoring
 Commercials
 ADR & Foley
 Sound & Picture Editorial
 Sound Design
 Video Game

2 ABOUT US
Vermilion Reel Works is located in the premiere South-Bund area of Shanghai. Occupying a 5000 square meter Technical Building, Vermilion Reel Works was built by a filmmaker for filmmakers, and is one of the largest, most versatile full-service post-production facilities in China.

Vermilion Reel Works is positioning to be at the forefront of the latest technology. Our goal is to provide a comprehensive solution for the post-production needs of our clients. We offer two fully-equipped dubbing stages (one of which will be certified KESTRON VOXAR PREMIERE), a large variety of both picture and sound editing rooms, impressive Foley and ADR stages, a world-class scoring stage, and complete audio and video transfer services.

We can handle your entire project from editing all the way to the end of the final sound mix; all under one extremely comfortable roof. We fully realize that the true art is in listening to the needs of our clients and making their greatest vision a reality. To this end our creative team's expertise, with a network of sound supervisors, editors and mixers, will deliver the magic you need. Producers and directors will also find our richly appointed guest accommodations to be a comfortable and soothing place to wind up the day. Every aspect of your project will be taken care of by a skilled and dedicated team, in the way that is best suited to you.

3 TEAM
(attachment 01)

4 SERVICES
Sound Mix
ADR
FOLEY
MUSIC
Sound Design
Sound Edit
Picture Edit
for all the Films, TV Drama, Commercials, Video Games, Online Media
(attachment 02, use photo)

5 FACILITY
(attachment 03)

6 CONTACT
(attachment04)
with map

Project Deadline Extended
Reason: Designers work are great, my bosses will spend 1-2 days select one of these web design, and spend 1-2 days to make some change, maybe use new photos.

```html
<!DOCTYPE html>
<html lang="en">
<head>
<meta charset="utf-8">
<title>Vermilion Reel Works</title>
<link rel="stylesheet" href="https://fonts.googleapis.com/css2?family=Roboto:wght@300;400;500&display=swap">
<style>
:root{
  --accent:#f05a3c;
  --ink:#2d2d2d;
  --text:#7a7a7a;
  --bar:#2a2a2a;
  --soft:#f5f5f5;
  --line:#e2e2e2;
  --white:#ffffff;
}
*{box-sizing:border-box;margin:0;padding:0}
html,body{width:1200px;height:2535px;overflow:hidden}
body{font-family:'Roboto',sans-serif;font-weight:300;color:var(--text);background:var(--white);position:relative}
.topbar{position:absolute;left:0;top:0;width:1200px;height:32px;background:var(--bar)}
.topbar .social{position:absolute;left:173px;top:6px;display:flex;gap:10px}
.topbar .social span{width:20px;height:20px;border:1px solid #888;border-radius:50%}
.topbar .lang{position:absolute;left:940px;top:8px;display:flex;align-items:center;gap:8px;color:#ddd;font-size:10px;font-weight:400;letter-spacing:.5px}
.topbar .lang i{width:14px;height:14px;border-radius:50%;background:#bbb;display:block}
.header{position:absolute;top:32px;left:0;width:1200px;height:126px;background:var(--white)}
.brand{position:absolute;left:171px;top:44px;display:flex;align-items:center;gap:14px}
.brand i{width:38px;height:38px;border-radius:50%;background:var(--accent);display:block}
.brand b{font-weight:400;font-size:23px;color:var(--accent);letter-spacing:.3px}
.nav{position:absolute;left:625px;top:56px;display:flex;gap:25px;font-size:15px;font-weight:400;color:#555}
.nav .active{color:var(--accent)}
.hero{position:absolute;top:158px;left:0;width:1200px;height:417px;background:linear-gradient(120deg,#1b1b1b 0%,#3a342e 40%,#55493d 65%,#2a2622 100%)}
.hero h1{position:absolute;top:124px;left:0;width:1200px;text-align:center;font-weight:400;font-size:38px;line-height:52px;color:var(--white)}
.hero h1 em{font-style:normal;color:var(--accent)}
.btn{display:inline-block;background:var(--accent);color:var(--white);font-size:14px;font-weight:400;text-align:center}
.hero .btn{position:absolute;left:539px;top:243px;width:122px;height:41px;line-height:41px}
.arrow{position:absolute;top:180px;width:56px;height:56px;border:3px solid var(--accent);border-radius:50%}
.arrow.prev{left:55px}.arrow.next{left:1084px}
.arrow svg{position:absolute;left:15px;top:15px}
.dots{position:absolute;top:378px;left:578px;display:flex;gap:8px}
.dots span{width:10px;height:10px;border-radius:50%;background:var(--white)}
.dots span:first-child{background:var(--accent)}
.welcome{position:absolute;top:575px;left:0;width:1200px;height:300px;border-bottom:1px solid var(--line)}
.welcome h2{position:absolute;left:171px;top:48px;font-weight:300;font-size:30px;line-height:38px;color:#555}
.welcome h2 span{display:block;color:var(--accent);font-size:33px}
.welcome p{position:absolute;left:175px;top:135px;width:520px;font-size:15px;line-height:24px}
.welcome .btn{position:absolute;left:171px;top:200px;width:125px;height:41px;line-height:41px}
.welcome .photo{position:absolute;left:815px;top:45px;width:200px;height:200px;border-radius:50%;border:22px solid var(--accent);background:radial-gradient(circle,#6b5a4a,#2e2822)}
.services{position:absolute;top:875px;left:0;width:1200px;height:572px;background:var(--soft);border-bottom:1px solid var(--line)}
.service{position:absolute;width:400px;height:120px}
.service .icon{position:absolute;left:0;top:0;width:114px;height:114px;border-radius:50%;border:7px solid var(--ink);background:var(--white);display:flex;align-items:center;justify-content:center}
.service h3{position:absolute;left:125px;top:12px;font-weight:400;font-size:20px;color:var(--accent)}
.service p{position:absolute;left:125px;top:44px;width:215px;font-size:14px;line-height:22px}
.work{position:absolute;top:1447px;left:0;width:1200px;height:778px}
.work h2{position:absolute;top:50px;width:1200px;text-align:center;font-weight:300;font-size:42px;color:var(--accent)}
.work p.lead{position:absolute;top:115px;width:1200px;text-align:center;font-size:18px;line-height:29px;color:#999}
.tile{position:absolute;width:226px;height:224px;background:linear-gradient(135deg,#1c1c1c,#3b3631 60%,#222);text-align:center}
.tile h4{margin-top:56px;font-weight:300;font-size:19px;color:var(--accent)}
.tile span{display:block;margin-top:6px;font-size:18px;color:var(--white)}
.tile i{display:block;width:40px;height:40px;margin:10px auto 0;border:2px solid var(--white);position:relative}
.tile i svg{position:absolute;left:9px;top:9px}
.footer{position:absolute;top:2225px;left:0;width:1200px;height:279px;background:linear-gradient(180deg,#0e0e0e,#1f1d1b 50%,#121212)}
.col{position:absolute;top:40px;height:200px}
.col+.col{border-left:1px solid #333}
.col h5{font-weight:300;font-size:26px;color:var(--accent);margin-bottom:16px}
.col li{list-style:none;font-size:12px;color:#ddd;font-weight:400;line-height:26px}
.col.social li{display:flex;align-items:center;gap:14px;line-height:36px}
.col.social li i{width:20px;height:20px;border-radius:50%;border:2px solid #ddd;display:block}
.col.news p{font-size:14px;color:#fff;font-weight:400}
.col.news .field{margin-top:14px;display:flex;width:222px;height:46px}
.col.news .field span{flex:1;background:var(--white);color:#999;font-size:11px;padding:16px 14px}
.col.news .field b{width:46px;background:var(--accent);display:flex;align-items:center;justify-content:center}
.col.news small{display:block;margin-top:8px;font-size:12px;line-height:16px;color:#eee;font-weight:400;width:190px}
.copy{position:absolute;top:2504px;left:0;width:1200px;height:31px;text-align:center;line-height:31px;font-size:11px;color:#444;font-weight:400}
</style>
</head>
<body>
<div class="topbar">
  <div class="social"><span></span><span></span><span></span></div>
  <div class="lang"><i></i>ENGLISH
    <svg width="10" height="6" viewBox="0 0 10 6"><path d="M1 1l4 4 4-4" fill="none" stroke="#999"/></svg></div>
</div>

<header class="header">
  <div class="brand"><i></i><b>VERMILION REEL WORKS</b></div>
  <nav class="nav"><span class="active">Home</span><span>About</span><span>Team</span><span>Services</span><span>Facility</span><span>Contact</span></nav>
</header>

<section class="hero" role="img" aria-label="Dimly lit post-production studio with mixing console and keyboard">
  <h1><em>Vermilion Reel Works</em> provides a well-designed<br>working environment !</h1>
  <span class="btn">Read More</span>
  <span class="arrow prev"><svg width="20" height="20" viewBox="0 0 20 20"><path d="M13 2L5 10l8 8" fill="none" stroke="#f05a3c" stroke-width="2.5"/></svg></span>
  <span class="arrow next"><svg width="20" height="20" viewBox="0 0 20 20"><path d="M7 2l8 8-8 8" fill="none" stroke="#f05a3c" stroke-width="2.5"/></svg></span>
  <div class="dots"><span></span><span></span><span></span></div>
</section>

<section class="welcome">
  <h2>Welcome To The<span>VERMILION REEL WORKS</span></h2>
  <p>Vermilion Reel Works provides a well-designed working environment which amplifies your team’s ability to reach their creative goals.</p>
  <span class="btn">Read More</span>
  <div class="photo" role="img" aria-label="Engineer working at a studio mixing desk"></div>
</section>

<section class="services">
  <div class="service" style="left:224px;top:65px">
    <div class="icon"><svg width="52" height="44" viewBox="0 0 52 44" fill="none" stroke="#2d2d2d" stroke-width="3"><rect x="2" y="2" width="48" height="40"/><path d="M13 2v40M39 2v40M2 12h11M2 22h11M2 32h11M39 12h11M39 22h11M39 32h11M13 22h26"/></svg></div>
    <h3>Feature Films</h3><p>Vermilion Reel Works provides a well-designed working environment !</p>
  </div>
  <div class="service" style="left:644px;top:65px">
    <div class="icon"><svg width="56" height="44" viewBox="0 0 56 44" fill="none" stroke="#2d2d2d" stroke-width="3"><rect x="2" y="2" width="52" height="32"/><path d="M20 42h16M28 34v8"/><circle cx="28" cy="18" r="8"/><path d="M26 14l5 4-5 4z" fill="#2d2d2d"/></svg></div>
    <h3>Commercials</h3><p>Vermilion Reel Works provides a well-designed working environment !</p>
  </div>
  <div class="service" style="left:224px;top:228px">
    <div class="icon"><svg width="34" height="54" viewBox="0 0 34 54" fill="none" stroke="#2d2d2d" stroke-width="3"><rect x="9" y="2" width="16" height="30" rx="8"/><path d="M3 24a14 14 0 0028 0M17 38v12M9 52h16M11 12h12M11 20h12"/></svg></div>
    <h3>ADR &amp; Foley</h3><p>Vermilion Reel Works provides a well-designed working environment !</p>
  </div>
  <div class="service" style="left:644px;top:228px">
    <div class="icon"><svg width="56" height="48" viewBox="0 0 56 48" fill="none" stroke="#2d2d2d" stroke-width="3"><rect x="2" y="34" width="52" height="10" rx="5"/><path d="M30 30L44 6l5 3-14 24z"/><path d="M10 39h4M20 39h4"/></svg></div>
    <h3>Design</h3><p>Vermilion Reel Works provides a well-designed working environment !</p>
  </div>
  <div class="service" style="left:224px;top:391px">
    <div class="icon"><svg width="50" height="50" viewBox="0 0 50 50"><path fill="#2d2d2d" d="M21 2h8l1 7 5 2 6-4 6 6-4 6 2 5 7 1v8l-7 1-2 5 4 6-6 6-6-4-5 2-1 7h-8l-1-7-5-2-6 4-6-6 4-6-2-5-7-1v-8l7-1 2-5-4-6 6-6 6 4 5-2z"/><circle cx="25" cy="25" r="8" fill="#fff"/></svg></div>
    <h3>Editing</h3><p>Vermilion Reel Works provides a well-designed working environment !</p>
  </div>
  <div class="service" style="left:644px;top:391px">
    <div class="icon"><svg width="54" height="50" viewBox="0 0 54 50" fill="none" stroke="#2d2d2d" stroke-width="3"><circle cx="22" cy="25" r="20"/><circle cx="22" cy="25" r="6" fill="#2d2d2d"/><path d="M44 14v26" /><circle cx="40" cy="40" r="5" fill="#2d2d2d"/><path d="M44 14l8 4"/></svg></div>
    <h3>Music &amp; Scoring</h3><p>Vermilion Reel Works provides a well-designed working environment !</p>
  </div>
</section>

<section class="work">
  <h2>What We Do</h2>
  <p class="lead">Vermilion Reel Works provides a well-designed working environment<br>which amplifies your team’s ability to reach their creative goals.</p>
  <div class="tile" style="left:211px;top:224px" role="img" aria-label="Close-up of a studio monitor speaker"><h4>Vermilion Reel Works</h4><span>Details</span><i><svg width="18" height="18" viewBox="0 0 18 18" fill="none" stroke="#fff" stroke-width="2"><circle cx="7" cy="7" r="5"/><path d="M11 11l5 5"/></svg></i></div>
  <div class="tile" style="left:490px;top:224px" role="img" aria-label="Mixing console faders"><h4>Vermilion Reel Works</h4><span>Details</span><i><svg width="18" height="18" viewBox="0 0 18 18" fill="none" stroke="#fff" stroke-width="2"><circle cx="7" cy="7" r="5"/><path d="M11 11l5 5"/></svg></i></div>
  <div class="tile" style="left:763px;top:224px" role="img" aria-label="Dubbing stage with screen"><h4>Vermilion Reel Works</h4><span>Details</span><i><svg width="18" height="18" viewBox="0 0 18 18" fill="none" stroke="#fff" stroke-width="2"><circle cx="7" cy="7" r="5"/><path d="M11 11l5 5"/></svg></i></div>
  <div class="tile" style="left:211px;top:491px" role="img" aria-label="Rack of audio equipment"><h4>Vermilion Reel Works</h4><span>Details</span><i><svg width="18" height="18" viewBox="0 0 18 18" fill="none" stroke="#fff" stroke-width="2"><circle cx="7" cy="7" r="5"/><path d="M11 11l5 5"/></svg></i></div>
  <div class="tile" style="left:490px;top:491px" role="img" aria-label="Control surface with coloured buttons"><h4>Vermilion Reel Works</h4><span>Details</span><i><svg width="18" height="18" viewBox="0 0 18 18" fill="none" stroke="#fff" stroke-width="2"><circle cx="7" cy="7" r="5"/><path d="M11 11l5 5"/></svg></i></div>
  <div class="tile" style="left:763px;top:491px" role="img" aria-label="Large format console in an editing room"><h4>Vermilion Reel Works</h4><span>Details</span><i><svg width="18" height="18" viewBox="0 0 18 18" fill="none" stroke="#fff" stroke-width="2"><circle cx="7" cy="7" r="5"/><path d="M11 11l5 5"/></svg></i></div>
</section>

<footer class="footer" role="img" aria-label="Dark blurred studio equipment backdrop">
  <div class="col" style="left:171px;width:130px"><h5>Menu</h5><ul><li>Home</li><li>About</li><li>Team</li><li>Services</li><li>Facility</li><li>Contact</li></ul></div>
  <div class="col" style="left:301px;width:222px;padding-left:60px"><h5>Services</h5><ul><li>Feature Films</li><li>Design</li><li>Music &amp; Scoring</li><li>Commercials</li><li>ADR &amp; Foley</li><li>Editing</li></ul></div>
  <div class="col social" style="left:523px;width:220px;padding-left:62px"><h5>Social</h5><ul><li><i></i>Friendsphere</li><li><i></i>Chirpline</li><li><i></i>Pinboardly</li></ul></div>
  <div class="col news" style="left:743px;width:300px;padding-left:64px"><h5>Newsletter</h5><p>Sign Up Our Newsletter Now</p>
    <div class="field"><span>Email</span><b><svg width="12" height="18" viewBox="0 0 12 18"><path d="M2 2l7 7-7 7" fill="none" stroke="#fff" stroke-width="2"/></svg></b></div>
    <small>Lorem ipsum dolor sit amet, consectetuer adipiscing elit, sed diam nonu</small></div>
</footer>
<div class="copy">All Rights Reserved © 2014 Vermilion Reel Works.</div>
</body>
</html>
```